Business card design needed

It's a new business in town.Something so the name stands out.I need a logo for the B.R.W
I may all so use the design as a sign on a building

Contact Information for Business Card

B.R.W
Brindlewood Auto Detailing
42 Fenwarra Crs
Brindlewood Vic 3799
Ph:(03)59284736
Mob:0417362958

```html
<!DOCTYPE html>
<html lang="en">
<head>
<meta charset="utf-8">
<title>Brindlewood Auto Detailing – Business Card</title>
<link href="https://fonts.googleapis.com/css2?family=Questrial&family=Didact+Gothic&display=swap" rel="stylesheet">
<style>
  :root {
    --card-bg: #000000;
    --brand-blue: #1f7bc6;
    --silver-light: #ffffff;
    --silver-mid: #cfcfcf;
    --silver-dark: #8a8a8a;
    --title-shadow: #5a5a5a;
    --contact-text: #8fa4b4;
  }
  html, body {
    margin: 0;
    padding: 0;
    width: 1200px;
    height: 693px;
    overflow: hidden;
    background: var(--card-bg);
  }
  .card {
    position: relative;
    width: 1200px;
    height: 693px;
    background: var(--card-bg);
    font-family: "Questrial", "Didact Gothic", sans-serif;
  }
  .brand-mark {
    position: absolute;
    top: 95px;
    left: 0;
    width: 100%;
    text-align: center;
    font-size: 120px;
    line-height: 1;
    letter-spacing: 6px;
    color: var(--brand-blue);
  }
  .business-name {
    position: absolute;
    top: 358px;
    left: 0;
    width: 100%;
    text-align: center;
    margin: 0;
    font-family: "Questrial", sans-serif;
    font-weight: 400;
    font-size: 98px;
    line-height: 1;
    letter-spacing: -2px;
    background: linear-gradient(180deg, var(--silver-light) 0%, var(--silver-mid) 45%, var(--silver-dark) 70%, var(--silver-light) 100%);
    -webkit-background-clip: text;
    background-clip: text;
    color: transparent;
    filter: drop-shadow(3px 12px 0 var(--title-shadow));
  }
  .contact {
    position: absolute;
    top: 518px;
    margin: 0;
    font-family: "Didact Gothic", sans-serif;
    font-style: normal;
    color: var(--contact-text);
    font-size: 32px;
    line-height: 37px;
  }
  .contact-address { left: 178px; letter-spacing: 1px; }
  .contact-phones { left: 722px; top: 536px; font-family: "Questrial", sans-serif; }
</style>
</head>
<body>
  <main class="card">
    <div class="brand-mark">B.R.W</div>
    <h1 class="business-name">Brindlewood Auto Detailing</h1>
    <address class="contact contact-address">
      42 Fenwarra Crs<br>
      Brindlewood<br>
      Vic 3799
    </address>
    <address class="contact contact-phones">
      Ph: (03) 5928 4736<br>
      Mob: 0417 362 958
    </address>
  </main>
</body>
</html>
```